TRI FOLD BROCHURE

I need a trifold brochure designed for my carpet cleaning company. It will be specifically for realtors and real estate attorneys. I have the text content I need in the brochure available as well as the company logo and a spotted dog picture we use in most of our marketing.

Industry/Entity Type

Real Estate

```html
<!DOCTYPE html>
<html lang="en">
<head>
<meta charset="utf-8">
<title>Brightway Floor Care – Tri-fold Brochure, Front</title>
<link rel="stylesheet" href="https://fonts.googleapis.com/css2?family=Open+Sans:wght@400;600;700&display=swap">
<style>
:root{
  --stage:#1e1e1e;
  --panel-dark:#2e2e2e;
  --panel-light:#e9e7e3;
  --ink:#222222;
  --ink-soft:#4a4a4a;
  --accent:#16a9b8;
  --green:#1cae4e;
  --white:#ffffff;
  --label:#cfcfcf;
}
*{margin:0;padding:0;box-sizing:border-box}
html,body{width:1200px;height:907px;overflow:hidden;background:var(--stage)}
body{font-family:"Open Sans",Arial,sans-serif;position:relative;color:var(--ink)}
.side-label{position:absolute;top:34px;left:0;width:1200px;text-align:center;color:var(--label);font-size:20px;font-weight:400}
.brochure{position:absolute;left:97px;top:97px;width:1009px;height:777px;background:var(--panel-dark)}
.panel{position:absolute;top:0;height:777px}

/* left panel */
.panel-left{left:0;width:336px;background:var(--panel-light)}
.hero-photo{position:absolute;left:0;top:0;width:336px;height:181px;background:linear-gradient(160deg,#f4f4f2 0%,#dcd8d2 55%,#c9b49d 100%)}
.hero-rule{position:absolute;left:0;top:181px;width:336px;height:5px;background:var(--panel-dark)}
.reasons{position:absolute;left:20px;top:204px;width:300px}
.reasons h2{font-size:20px;line-height:29px;font-weight:600;color:var(--ink)}
.reasons h2 .brand{color:var(--accent)}
.reasons p{font-size:12px;line-height:16px;margin-top:14px;color:var(--ink-soft)}
.benefits{list-style:none;margin-top:22px}
.benefits li{font-size:12px;line-height:16px;color:var(--ink-soft);position:relative;padding-left:11px;margin-bottom:9px}
.benefits li::before{content:"";position:absolute;left:0;top:7px;width:3px;height:3px;border-radius:50%;background:var(--ink-soft)}
.benefits .green{color:var(--green);font-weight:700}
.phone-tab{position:absolute;left:20px;bottom:0;width:296px;height:59px;background:var(--panel-dark);border-radius:28px 28px 0 0;color:var(--white);font-weight:700;font-size:22px;text-align:center;line-height:56px}

/* middle panel */
.panel-middle{left:336px;width:334px;background:var(--panel-dark)}
.wordmark-vertical{position:absolute;left:167px;top:330px;transform:translate(-50%,-50%) rotate(-90deg);white-space:nowrap;color:var(--white);font-weight:700;font-size:46px;letter-spacing:2px}
.middle-phone{position:absolute;left:0;top:704px;width:334px;text-align:center;color:var(--white);font-weight:700;font-size:28px}

/* right panel */
.panel-right{left:670px;width:339px;height:749px;background:var(--panel-light);overflow:hidden}
.wordmark{position:absolute;left:0;top:40px;width:339px;text-align:center;font-weight:700;font-size:26px;color:var(--ink-soft);letter-spacing:1px}
.house-photo{position:absolute;left:0;top:0}
.call-today{position:absolute;left:0;top:628px;width:339px;text-align:center;font-size:28px;color:var(--ink-soft)}
.right-phone{position:absolute;left:0;top:668px;width:339px;text-align:center;font-size:30px;font-weight:700;color:var(--ink-soft)}
</style>
</head>
<body>
<div class="side-label">Front</div>

<main class="brochure">
  <section class="panel panel-left">
    <div class="hero-photo" role="img" aria-label="Photo of a smiling child lying on a clean white carpet beside a small dog"></div>
    <div class="hero-rule"></div>
    <div class="reasons">
      <h2>Reasons&nbsp; Why Homeowners<br>Love <span class="brand">Brightway Floor Care</span></h2>
      <p>No cleaning method can promise 100% removal of contaminates in your carpet.</p>
      <p>However, our proprietary cleaning system has been repeatedly tested and proven to produce results that are at least 25% cleaner than even the most powerful steam cleaning systems available</p>
      <ul class="benefits">
        <li><span class="green">GREEN</span> cleaning agents.</li>
        <li>Efficient, your time is valuable.</li>
        <li>Dry in ONE hour.</li>
        <li>No hoses drag through the house.</li>
        <li>No doors left open during the cleaning.</li>
        <li>Patented hyper agitation that gets the carpet 25% cleaner on average than the best steam cleaning truck mount system available today.</li>
        <li>Green cleaning agent that keeps microbial and pathogens from regrowing in the damp carpet after the cleaning is completed, unlike steam cleaning.</li>
      </ul>
    </div>
    <div class="phone-tab">1-800-555-0142</div>
  </section>

  <section class="panel panel-middle">
    <div class="wordmark-vertical">BRIGHTWAY FLOOR CARE</div>
    <div class="middle-phone">1-800-555-0142</div>
  </section>

  <section class="panel panel-right">
    <div class="wordmark">BRIGHTWAY FLOOR CARE</div>
    <svg class="house-photo" width="339" height="749" viewBox="0 0 339 749">
      <defs>
        <linearGradient id="house-tones" x1="0" y1="0" x2="0" y2="1">
          <stop offset="0" stop-color="#3d7bd0"/>
          <stop offset="0.3" stop-color="#d9d2c8"/>
          <stop offset="0.65" stop-color="#b9a596"/>
          <stop offset="1" stop-color="#4f8f2e"/>
        </linearGradient>
      </defs>
      <circle cx="220" cy="362" r="221" fill="var(--panel-dark)"/>
      <circle cx="220" cy="362" r="213" fill="url(#house-tones)" role="img" aria-label="Photo of a suburban house with a sold sign on the front lawn"/>
    </svg>
    <div class="call-today">Call Us Today</div>
    <div class="right-phone">1-800-555-0142</div>
  </section>
</main>
</body>
</html>
```